Real Estate Valuation Services

format
A5 portrait, look at the picture
Double-sided: Front = visual & emotional, Back = informative & structured.
goal
Highlight the free hedonic property valuation as the main offer.
Build trust by presenting the company as an exclusive, family-owned real estate firm with local roots in Meilen/ZH.
Communicate the USP “Everything from one source” clearly – from valuation to notary support and tax guidance.
Target audience
Homeowners in the Lake Zurich region considering selling their property.
Clients who value exclusivity, professionalism, and personal service.
Design style
Modern, clean, elegant – plenty of white space. Look at the website: https://brunnhofwohnen.ch/
Tone: Professional, trustworthy, exclusive – not like a mass-market flyer.
If possible, the text should be in German. Contact details must be included:
info@brunnhofwohnen.ch
+41 77 562 18 04
Target Market(s)
property owner
Industry/Entity Type
real estate
Look and feel

```html
<!DOCTYPE html>
<html lang="en">
<head>
<meta charset="utf-8">
<title>Brunnhof Wohnen – Free Hedonic Property Valuation</title>
<link href="https://fonts.googleapis.com/css2?family=Montserrat:wght@300;400;600;700;800&display=swap" rel="stylesheet">
<style>
  :root {
    --green-dark: #1f9553;
    --green-mid: #3fae4f;
    --green-light: #8cc63f;
    --ink: #1d1d1b;
    --text: #3c3c3c;
    --paper: #ffffff;
    --backdrop: #eceeea;
    --sky: #b9cde0;
    --hill: #6f6a5c;
  }
  * { margin: 0; padding: 0; box-sizing: border-box; }
  html, body { width: 855px; height: 1200px; overflow: hidden; }
  body {
    background: var(--backdrop);
    font-family: "Montserrat", Arial, sans-serif;
    color: var(--text);
    position: relative;
  }
  .sheet {
    position: absolute;
    top: 313px;
    width: 405px;
    height: 573px;
    background: var(--paper);
    overflow: hidden;
    box-shadow: 0 4px 14px rgba(0,0,0,.15);
  }
  .sheet--front { left: 15px; }
  .sheet--back { left: 435px; }
  .sheet__art { position: absolute; inset: 0; width: 405px; height: 573px; }
  .abs { position: absolute; }
  .site-url { top: 20px; right: 32px; font-size: 7px; color: #fff; font-weight: 400; }

  /* front */
  .front__free { left: 200px; top: 272px; font-size: 52px; font-weight: 800; color: var(--green-dark); letter-spacing: -1px; line-height: 1; }
  .front__sub { right: 40px; top: 352px; font-size: 12.5px; font-weight: 600; color: var(--ink); }
  .front__intro { left: 32px; top: 386px; width: 350px; font-size: 9.4px; line-height: 12.8px; font-weight: 400; }
  .brand { left: 0; right: 0; top: 455px; display: flex; justify-content: center; align-items: center; gap: 8px; }
  .brand__mark { width: 14px; height: 14px; background: var(--green-dark); }
  .brand__name { font-size: 24px; font-weight: 700; color: var(--green-dark); }
  .contact-bar { left: 48px; right: 48px; top: 530px; height: 25px; border-top: 1px solid var(--green-light); border-bottom: 1px solid var(--green-light); display: flex; justify-content: center; align-items: center; gap: 14px; font-size: 8.5px; font-weight: 700; color: var(--ink); }
  .contact-item { display: flex; align-items: center; gap: 6px; }
  .icon-dot { width: 11px; height: 11px; }

  /* back */
  .back__free { left: 34px; top: 100px; font-size: 40px; font-weight: 800; color: var(--green-dark); line-height: 1; letter-spacing: -.5px; }
  .back__sub { left: 34px; top: 143px; font-size: 15.5px; font-weight: 700; color: var(--green-light); }
  .back__intro { left: 34px; top: 190px; width: 215px; font-size: 9px; line-height: 12.6px; }
  .feature { left: 24px; width: 240px; display: flex; gap: 16px; align-items: flex-start; }
  .feature svg { flex: none; width: 36px; height: 36px; }
  .feature p { font-size: 8px; line-height: 11.5px; padding-top: 2px; }
  .feature--1 { top: 283px; }
  .feature--2 { top: 343px; }
  .feature--3 { top: 405px; }
  .testimonial { left: 272px; top: 210px; width: 120px; height: 160px; }
  .testimonial__text { position: absolute; left: 4px; top: 48px; width: 100px; font-size: 5.7px; line-height: 8px; }
  .testimonial__label { position: absolute; left: 4px; top: 130px; font-size: 5.5px; font-weight: 700; color: var(--ink); }
  .testimonial__stars { position: absolute; left: 3px; top: 139px; font-size: 8px; color: var(--ink); letter-spacing: 1px; }
  .back__note { left: 30px; top: 452px; width: 220px; font-size: 5.6px; line-height: 7.6px; }
  .back__brand { left: 37px; top: 476px; font-size: 15px; font-weight: 700; color: var(--green-dark); }
  .back__contacts { left: 37px; top: 503px; display: flex; flex-direction: column; gap: 7px; font-size: 8.3px; font-weight: 700; color: var(--ink); }
  .social { display: inline-flex; gap: 5px; margin-left: 12px; }
  .social span { width: 10px; height: 10px; border-radius: 50%; background: var(--green-mid); display: inline-block; }
  .portrait { left: 256px; top: 392px; width: 138px; height: 173px; border-radius: 60px 60px 0 0; background: linear-gradient(180deg, #f1f1f1 0%, #d9c2a2 45%, #2a2a2a 100%); }
</style>
</head>
<body>

<!-- Front side -->
<section class="sheet sheet--front">
  <svg class="sheet__art" viewBox="0 0 405 573" aria-hidden="true">
    <defs>
      <linearGradient id="head-f" x1="0" x2="1" y1="0" y2="0">
        <stop offset="0" stop-color="#8cc63f"/>
        <stop offset="1" stop-color="#1f9553"/>
      </linearGradient>
      <linearGradient id="band-f" x1="0" x2="1">
        <stop offset="0" stop-color="#1f9553"/>
        <stop offset=".5" stop-color="#3fae4f"/>
        <stop offset="1" stop-color="#8cc63f"/>
      </linearGradient>
    </defs>
    <path d="M0 0 H405 V122 C330 70 220 80 0 30 Z" fill="url(#head-f)"/>
    <path d="M0 24 C220 74 330 64 405 116 V130 C330 80 220 88 0 50 Z" fill="url(#band-f)"/>
  </svg>
  <div class="abs" role="img" aria-label="Photo of the agent standing by a fence above a lakeside town with snowy mountains behind"
       style="left:0;top:0;width:405px;height:345px;background:linear-gradient(180deg,#c6d8ea 20%,#a9bfd2 42%,#8a8474 62%,#5e5a50 100%);clip-path:path('M0 50 C220 88 330 80 405 130 V320 C330 330 260 325 190 338 C120 345 60 340 0 340 Z');"></div>
  <div class="abs" style="left:190px;top:265px;width:192px;height:66px;background:rgba(255,255,255,.9);"></div>
  <svg class="sheet__art" viewBox="0 0 405 573" aria-hidden="true">
    <path d="M0 340 C60 340 120 345 190 334 C260 325 330 328 405 318 V345 H0 Z" fill="#fff"/>
  </svg>
  <div class="abs site-url">brunnhofwohnen.ch</div>
  <div class="abs front__free">FREE!</div>
  <div class="abs front__sub">hedonic property valuation</div>
  <p class="abs front__intro">From a free, market-based valuation of your property to the creation\ of a customized marketing plan and the successful signing of the contract, we offer all services precisely tailored to your wishes and needs.</p>
  <div class="abs brand"><span class="brand__mark"></span><span class="brand__name">Brunnhof Wohnen</span></div>
  <div class="abs contact-bar">
    <span class="contact-item">
      <svg class="icon-dot" viewBox="0 0 12 12"><circle cx="6" cy="6" r="6" fill="#8cc63f"/><path d="M4 3.5 L5 5 L4.6 5.6 C5 6.6 5.6 7.2 6.4 7.5 L7 7 L8.5 8 L8 9 C5.6 9 3 6.4 3 4 Z" fill="#fff"/></svg>
      +41 77 562 18 04
    </span>
    <span class="contact-item">
      <svg class="icon-dot" viewBox="0 0 12 12"><circle cx="6" cy="6" r="6" fill="#8cc63f"/><rect x="3" y="4" width="6" height="4.2" fill="none" stroke="#fff" stroke-width=".9"/><path d="M3 4 L6 6.3 L9 4" fill="none" stroke="#fff" stroke-width=".9"/></svg>
      info@brunnhofwohnen.ch
    </span>
  </div>
</section>

<!-- Back side -->
<section class="sheet sheet--back">
  <svg class="sheet__art" viewBox="0 0 405 573" aria-hidden="true">
    <defs>
      <linearGradient id="head-b" x1="0" x2="1">
        <stop offset="0" stop-color="#8cc63f"/>
        <stop offset="1" stop-color="#1f9553"/>
      </linearGradient>
      <linearGradient id="band-b" x1="0" x2="1">
        <stop offset="0" stop-color="#1f9553"/>
        <stop offset=".55" stop-color="#3fae4f"/>
        <stop offset="1" stop-color="#8cc63f"/>
      </linearGradient>
    </defs>
    <path d="M0 0 H405 V132 C330 70 220 80 0 30 Z" fill="url(#head-b)"/>
    <path d="M0 24 C220 74 330 64 405 126 V138 C330 84 220 90 0 52 Z" fill="url(#band-b)"/>
    <rect x="0" y="565" width="320" height="8" fill="#8cc63f"/>
    <rect x="320" y="565" width="85" height="8" fill="#1f9553"/>
  </svg>
  <div class="abs site-url">brunnhofwohnen.ch</div>
  <div class="abs back__free">FREE!</div>
  <div class="abs back__sub">hedonic property valuation</div>
  <p class="abs back__intro">From a free, market-based valuation of your property to the creation\ of a customized marketing plan and the successful signing of the contract, we offer all services precisely tailored to your wishes and needs.</p>

  <div class="abs feature feature--1">
    <svg viewBox="0 0 36 36"><path d="M3 16 L18 4 L33 16" fill="none" stroke="#8cc63f" stroke-width="2.5"/><rect x="7" y="15" width="22" height="18" fill="none" stroke="#8cc63f" stroke-width="2.5"/><rect x="13" y="20" width="10" height="13" fill="#8cc63f"/><line x1="13" y1="24" x2="23" y2="24" stroke="#fff"/><line x1="13" y1="28" x2="23" y2="28" stroke="#fff"/></svg>
    <p>Lorem ipsum dolor sit amet, consectetur adipiscing elit. Proin auctor risus sed metus convallis, eget faucibus risus tincidunt.</p>
  </div>
  <div class="abs feature feature--2">
    <svg viewBox="0 0 36 36"><path d="M10 2 C5 2 3 6 3 9 C3 14 10 20 10 20 C10 20 17 14 17 9 C17 6 15 2 10 2 Z" fill="#8cc63f"/><circle cx="10" cy="9" r="3" fill="#fff"/><path d="M6 22 V34 H30 V22 L24 18 V24 L17 20 V34" fill="none" stroke="#8cc63f" stroke-width="2.5"/></svg>
    <p>Donec eget augue mollis, vestibulum eros a, pretium ligula. In ut enim eget nulla aliquet placerat. Vestibulum ac orci nec arcu faucibus ultrices.</p>
  </div>
  <div class="abs feature feature--3">
    <svg viewBox="0 0 36 36"><path d="M6 3 H26 V18 M26 28 V33 H6 Z" fill="none" stroke="#8cc63f" stroke-width="2.5"/><line x1="10" y1="10" x2="21" y2="10" stroke="#8cc63f" stroke-width="2"/><line x1="10" y1="15" x2="21" y2="15" stroke="#8cc63f" stroke-width="2"/><line x1="10" y1="20" x2="17" y2="20" stroke="#8cc63f" stroke-width="2"/><path d="M19 30 L31 17 L34 20 L22 33 L18 34 Z" fill="#8cc63f"/></svg>
    <p>Fusce iaculis arcu eu interdum auctor. Fusce dignissim purus sed diam egestas rutrum.</p>
  </div>

  <div class="abs testimonial">
    <svg width="120" height="160" viewBox="0 0 120 160" aria-hidden="true">
      <text x="0" y="52" font-family="Montserrat, Arial, sans-serif" font-size="68" font-weight="800" fill="#8cc63f">“</text>
      <polyline points="50,20 112,20 112,118" fill="none" stroke="#9a9a9a" stroke-width=".8"/>
      <text x="64" y="190" font-family="Montserrat, Arial, sans-serif" font-size="68" font-weight="800" fill="#8cc63f" transform="translate(0,-30)">”</text>
    </svg>
    <p class="testimonial__text">Lorem ipsum dolor sit amet, consectetur adipiscing elit. Fusce mollis velit vitae suscipit rhoncus. Duis libero turpis, porta in massa eget, posuere sollicitudin tellus. Cras lacinia nisi ut luctus malesuada.</p>
    <span class="testimonial__label">Client Testimonials</span>
    <span class="testimonial__stars">★★★★★</span>
  </div>

  <p class="abs back__note">Lorem ipsum dolor sit amet, consectetur adipiscing elit. Fusce mollis velit vitae suscipit rhoncus. Duis libero turpis</p>
  <div class="abs back__brand">Brunnhof Real Estate</div>
  <div class="abs back__contacts">
    <span class="contact-item">
      <svg class="icon-dot" viewBox="0 0 12 12"><circle cx="6" cy="6" r="6" fill="#8cc63f"/><path d="M4 3.5 L5 5 L4.6 5.6 C5 6.6 5.6 7.2 6.4 7.5 L7 7 L8.5 8 L8 9 C5.6 9 3 6.4 3 4 Z" fill="#fff"/></svg>
      &nbsp;+41 77 562 18 04
    </span>
    <span class="contact-item">
      <svg class="icon-dot" viewBox="0 0 12 12"><circle cx="6" cy="6" r="6" fill="#8cc63f"/><rect x="3" y="4" width="6" height="4.2" fill="none" stroke="#fff" stroke-width=".9"/><path d="M3 4 L6 6.3 L9 4" fill="none" stroke="#fff" stroke-width=".9"/></svg>
      &nbsp;info@brunnhofwohnen.ch
      <span class="social"><span></span><span></span></span>
    </span>
  </div>
  <div class="abs portrait" role="img" aria-label="Portrait photo of the agent in a dark blazer"></div>
</section>

</body>
</html>
```